International freight forwarder experienced in perishable handling needs a web design

We need a website designed that will allow us to capture more customers through the website. We would like a visually appealing design that is not so heavy on text. Our business covers the logistics and freight forwarding industries and we have offices in South America and the USA. Our main customers are importers USA, Europe, Asia and Russia and we currently work almost exclusively with perishable products such as fresh cut flowers, fresh exotics fruits, cacao, fresh fish etc. We would like to convey a fresh, modern approach to freight forwarding focusing on concepts such as - time sensitive, anytime-anywhere delivery, innovation, experience, reliability and confidence. Should include links with Plumetta and Worvanet. Our core solutions include: Core Services
*Air Freight
*Ocean Freight
*Warehousing & Distribution
Our industry solutions cover
*Flowers
*FMCG including, fruits, vegetables
*Live animals
*Automotive
*Consumer Goods
*Industrial
*Oil & Gas
*Pharma
* Event logistics
* Project logistics

Target Market(s)

Importers in Europe, USA, Asia, Middle East and Russia

Number of Pages Required

4 page

Font styles to use
Sans Serif

Colors
a1cd39
606060
000000

Requirements
Must have
• Photos of fresh cut flowers, FMCG such as cacao, fresh fish (packaged for shipping), fresh exotic fruits, pharma products (packaged for shipping), oil and gas etc. Internal customer login access
Nice to have
• Photos of cargo shipping carriers and cargo airline carriers. Features similar to those of following website http://www.brolvacargo.com/eng/main/index.jsp?FromURL=web
Should not have
• Too much text, needs to be visually pleasing

```html
<!DOCTYPE html>
<html lang="en">
<head>
<meta charset="utf-8">
<title>Verdanq Alliance Group — Freight Services</title>
<link href="https://fonts.googleapis.com/css2?family=Source+Sans+3:wght@400;600;700;800&display=swap" rel="stylesheet">
<style>
:root{
  --green:#8cc63e;
  --green-dark:#5f9a1f;
  --green-mid:#78b52c;
  --ink:#2d2d2d;
  --grey:#606060;
  --light:#f5f5f5;
  --line:#dedede;
  --dark:#2f2f2f;
  --darker:#222;
  --white:#fff;
}
*{box-sizing:border-box;margin:0;padding:0}
html,body{width:1200px;height:2286px;overflow:hidden}
body{font-family:"Source Sans 3",sans-serif;color:var(--grey);background:var(--white);position:relative}
.wrap{position:absolute;left:200px;width:800px}
a{color:inherit;text-decoration:none}

/* top bar */
.topbar{position:absolute;top:0;left:0;width:1200px;height:24px;background:var(--white)}
.social{position:absolute;left:200px;top:0;height:24px;width:114px;background:var(--dark);display:flex;gap:6px;align-items:center;padding-left:8px}
.social span{width:20px;height:14px;display:flex;align-items:center;justify-content:center}
.social i{display:block;width:9px;height:9px;background:#cfcfcf;border-radius:2px}
.contact-line{position:absolute;right:200px;top:0;height:24px;width:360px;background:var(--dark);color:#ddd;font-size:10px;display:flex;gap:20px;align-items:center;justify-content:flex-end;padding-right:8px}
.contact-line svg{vertical-align:-2px;margin-right:4px}

/* header */
.header{position:absolute;top:24px;left:0;width:1200px;height:104px}
.brand{position:absolute;left:200px;top:18px;display:flex;align-items:center;gap:8px}
.brand-dot{width:34px;height:34px;border-radius:50%;background:var(--green)}
.brand-name{font-size:22px;font-weight:700;color:var(--ink);line-height:1}
.brand-sub{position:absolute;left:240px;top:64px;font-size:8px;letter-spacing:2px;color:#999}
.nav{position:absolute;left:452px;top:47px;display:flex;font-size:12px;font-weight:600;color:var(--ink)}
.nav a{padding:0 8px;border-left:1px solid #ccc;line-height:12px}
.nav a:first-child{border:0;padding-left:0;color:var(--green)}
.locate{position:absolute;left:783px;top:37px;width:217px;height:34px;background:var(--green);color:var(--white);font-size:10px;font-weight:600;display:flex;align-items:center}
.locate b{flex:1;padding-left:16px;font-weight:600}
.locate span{width:32px;height:34px;background:var(--green-dark);display:flex;align-items:center;justify-content:center}

/* hero */
.hero{position:absolute;top:128px;left:0;width:1200px;height:369px;background:linear-gradient(180deg,#bcd8ef 0%,#d9dde0 30%,#9c8a7a 60%,#6f6a66 100%)}
.hero-card{position:absolute;left:615px;top:163px;width:385px;height:150px;background:rgba(255,255,255,.93);padding:18px 22px}
.hero-card h1{font-size:34px;font-weight:700;line-height:37px;color:var(--ink);letter-spacing:.5px}
.btn-green{display:inline-block;background:var(--green);color:var(--white);font-size:12px;font-weight:600;padding:9px 15px;margin-top:10px}
.hero-arrow{position:absolute;top:167px;width:36px;height:36px;background:rgba(0,0,0,.35);display:flex;align-items:center;justify-content:center}

/* welcome */
.welcome{position:absolute;top:497px;left:0;width:1200px;height:324px}
.welcome h2{position:absolute;left:200px;top:50px;font-size:32px;font-weight:800;line-height:41px;color:#7a7a7a}
.welcome h2 em{font-style:normal;color:var(--green)}
.welcome .btn-green{position:absolute;left:200px;top:230px;margin:0;padding:9px 14px}
.welcome-text{position:absolute;left:434px;top:52px;width:566px;font-size:11.4px;line-height:19px}
.welcome-text p+p{margin-top:18px}

/* services */
.services{position:absolute;top:821px;left:0;width:1200px;height:448px;background:radial-gradient(ellipse at 50% 45%,#86c23a 0%,var(--green-mid) 40%,var(--green-dark) 100%);color:var(--white)}
.map-area{position:absolute;left:300px;top:60px;width:600px;height:330px;background:radial-gradient(ellipse,rgba(255,255,255,.12),rgba(255,255,255,0) 70%)}
.section-title{text-align:center;font-size:23px;font-weight:700;letter-spacing:.5px}
.section-title:after{content:"";display:block;width:40px;height:2px;background:currentColor;margin:6px auto 0}
.services .section-title{position:absolute;top:34px;width:1200px}
.service{position:absolute;width:310px;padding-left:70px}
.service svg{position:absolute;left:0;top:0}
.service h3{font-size:15px;font-weight:700;margin-top:6px;margin-bottom:10px}
.service p{font-size:10.4px;line-height:16px;color:#eef6e2}
.service p b{color:var(--white)}
.btn-outline{position:absolute;left:518px;top:375px;width:164px;height:35px;border:2px solid var(--white);font-size:12px;font-weight:600;display:flex;align-items:center;justify-content:center;gap:10px}

/* partners */
.partners{position:absolute;top:1269px;left:0;width:1200px;height:209px}
.partners .section-title{position:absolute;top:45px;width:1200px;color:var(--ink)}
.partners .section-title em{font-style:normal;color:var(--green)}
.partners .section-title:after{background:var(--ink)}
.badges{position:absolute;left:200px;top:100px;width:800px;height:60px;display:flex;justify-content:space-between;align-items:center}
.badge{background:#e4e6ea}

/* clients */
.clients{position:absolute;top:1478px;left:0;width:1200px;height:389px;background:var(--dark);color:var(--white)}
.clients .section-title{position:absolute;top:27px;width:1200px}
.clients-sub{position:absolute;top:82px;width:1200px;text-align:center;font-size:12px;font-weight:700}
.quote{position:absolute;left:286px;top:118px;width:628px;height:119px;background:var(--darker);padding:20px 26px;font-size:11.4px;line-height:19px;color:#ddd}
.quote cite{display:block;font-style:normal;color:var(--green);font-weight:600;margin-top:6px}
.quote:after{content:"";position:absolute;left:50%;bottom:-12px;margin-left:-12px;border:12px solid transparent;border-bottom:0;border-top-color:var(--darker)}
.thumbs{position:absolute;left:423px;top:274px;display:flex;gap:4px}
.thumb{width:68px;height:72px;background:linear-gradient(180deg,#8a8a8a,#5b5b5b)}
.thumb.active{background:linear-gradient(180deg,#f2f2f2,#c9c9c9);border:3px solid var(--white);border-bottom-color:var(--green)}
.circle-arrow{position:absolute;top:300px;width:24px;height:24px;border:2px solid var(--white);border-radius:50%;display:flex;align-items:center;justify-content:center}

/* footer */
.footer{position:absolute;top:1867px;left:0;width:1200px;height:352px;background:var(--light)}
.footer h4{font-size:17px;font-weight:700;color:var(--ink);margin-bottom:14px}
.col-links{position:absolute;left:200px;top:30px;width:145px}
.col-links a{display:block;font-size:11.4px;line-height:32px;border-bottom:1px solid var(--line)}
.col-links a:last-child{border:0}
.col-about{position:absolute;left:381px;top:30px;width:300px;font-size:11.4px;line-height:19px}
.col-about p+p{margin-top:18px}
.tweet{position:absolute;left:200px;top:278px;width:417px;height:44px;background:#e6e6e6;display:flex;align-items:center;gap:14px;padding-left:20px;font-size:10.5px;font-style:italic}
.tweet i{width:18px;height:18px;border-radius:50%;background:#3aa0d8}
.col-news{position:absolute;left:692px;top:30px;width:308px}
.news{display:flex;gap:16px;padding:10px 0 12px;border-bottom:1px solid var(--line)}
.news:last-child{border:0}
.date{width:36px;height:40px;background:var(--green);color:var(--white);text-align:center;font-size:7px;line-height:10px;padding-top:3px}
.date b{display:block;font-size:17px;line-height:22px}
.news p{font-size:11.4px;line-height:19px}
.news a{display:block;color:var(--green);font-size:11.4px;margin-top:8px}
.bottombar{position:absolute;top:2225px;left:0;width:1200px;height:61px;border-top:1px solid var(--line);font-size:8.5px;color:#555}
.bottombar .legal{position:absolute;left:200px;top:24px}
.bottombar .legal a{padding:0 8px;border-left:1px solid #999}
.bottombar .legal a:first-child{border:0;padding-left:0}
.bottombar .copy{position:absolute;right:200px;top:24px}
</style>
</head>
<body>

<div class="topbar">
  <div class="social">
    <span aria-label="Plumetta"><i></i></span>
    <span aria-label="Chirpel"><i></i></span>
    <span aria-label="Vidora"><i></i></span>
    <span aria-label="Worvanet"><i></i></span>
  </div>
  <div class="contact-line">
    <span><svg width="10" height="10" viewBox="0 0 10 10"><path d="M2 1l2 2-1 1.5c.6 1.2 1.4 2 2.5 2.5L7 6l2 2-1.2 1.5C4.5 9 1 5.5.5 2.2z" fill="#ddd"/></svg>Call Us: 100 555 0142</span>
    <span><svg width="11" height="8" viewBox="0 0 11 8"><rect width="11" height="8" fill="#ddd"/><path d="M0 0l5.5 4.5L11 0" stroke="#2f2f2f" fill="none"/></svg>Email Us: contact@verdanqalliance.com</span>
  </div>
</div>

<header class="header">
  <div class="brand"><div class="brand-dot"></div><div class="brand-name">Verdanq Alliance</div></div>
  <div class="brand-sub">GROUP</div>
  <nav class="nav"><a>HOME</a><a>ABOUT US</a><a>SERVICES</a><a>CONTAINER</a><a>CONTACT</a></nav>
  <a class="locate"><b>LOCATE AN OFFICE CLOSE TO YOU</b><span><svg width="10" height="6" viewBox="0 0 10 6"><path d="M1 1l4 4 4-4" stroke="#fff" stroke-width="1.6" fill="none"/></svg></span></a>
</header>

<section class="hero" role="img" aria-label="Photo: ground crew loading stacked perishable cargo pallets beside a cargo aircraft">
  <div class="hero-arrow" style="left:0"><svg width="10" height="16" viewBox="0 0 10 16"><path d="M8 1L2 8l6 7" stroke="#fff" stroke-width="2" fill="none"/></svg></div>
  <div class="hero-arrow" style="right:0"><svg width="10" height="16" viewBox="0 0 10 16"><path d="M2 1l6 7-6 7" stroke="#fff" stroke-width="2" fill="none"/></svg></div>
  <div class="hero-card">
    <h1>PROVIDE FIRST CLASS FREIGHT SERVICES</h1>
    <a class="btn-green">GET STARTED WITH US &nbsp;›</a>
  </div>
</section>

<section class="welcome">
  <h2>WELCOME<br>TO <em>VERDANQ</em><br>ALLIANCE<br><em>GROUP</em></h2>
  <a class="btn-green">READ MORE &nbsp;&nbsp;›</a>
  <div class="welcome-text">
    <p>Lorem ipsum dolor sit amet, consectetur adipiscing elit. Morbi accumsan dolor non faucibus finibus. Maecenas nec elit accumsan, bibendum elit in, eleifend enim. Nulla feugiat lectus velit, quis congue odio dapibus sed. Aenean vel suscipit enim, sit amet mollis mauris. Vestibulum quis tortor nec nisi ornare scelerisque vitae suscipit ipsum. Phasellus vel scelerisque tortor. Vivamus euismod suscipit sem a aliquam. Mauris auctor elit nunc, vitae facilisis nisl ornare nec. Pellentesque ac ante non ipsum aliquet dignissim.</p>
    <p>Mauris semper vehicula orci, et mattis nulla. Cras eu enim lobortis, molestie augue nec, molestie ante. Vestibulum molestie consectetur tellus vitae feugiat. Sed eget neque in tellus interdum bibendum vitae non tellus. Praesent quam nisl, lacinia vitae sagittis et, accumsan ut lacus. Vestibulum quis tortor nec nisi ornare scelerisque vitae suscipit ipsum. Phasellus vel scelerisque tortor. Vivamus euismod suscipit sem a aliquam. Mauris auctor elit nunc, vitae facilisis nisl ornare nec. Pellentesque ac ante non ipsum aliquet dignissim.</p>
  </div>
</section>

<section class="services">
  <div class="map-area" role="img" aria-label="Faint world map in the background"></div>
  <h2 class="section-title">OUR SERVICES</h2>

  <div class="service" style="left:200px;top:105px">
    <svg width="54" height="44" viewBox="0 0 54 44" fill="#fff"><rect x="16" y="4" width="8" height="8"/><rect x="26" y="4" width="8" height="8"/><rect x="14" y="14" width="22" height="8"/><path d="M2 24h50l-7 10H8z"/><path d="M2 40q6-4 12 0t13 0 13 0 12 0" stroke="#fff" stroke-width="2" fill="none"/></svg>
    <h3>SEA FREIGHT</h3>
    <p>Mauris semper vehicula orci, et mattis nulla. Cras eu enim lobortis, molestie augue nec, molestie ante. Vestibulum molestie consectetur tellus vitae feugiat. <b>Read More...</b></p>
  </div>
  <div class="service" style="left:634px;top:105px">
    <svg width="56" height="44" viewBox="0 0 56 44" fill="#fff"><rect x="2" y="6" width="32" height="24"/><path d="M36 14h10l8 9v11H36z"/><circle cx="12" cy="36" r="5"/><circle cx="26" cy="36" r="5"/><circle cx="46" cy="36" r="5"/></svg>
    <h3>ROAD FREIGHT</h3>
    <p>Mauris semper vehicula orci, et mattis nulla. Cras eu enim lobortis, molestie augue nec, molestie ante. Vestibulum molestie consectetur tellus vitae feugiat. <b>Read More...</b></p>
  </div>
  <div class="service" style="left:200px;top:246px">
    <svg width="44" height="50" viewBox="0 0 44 50" fill="#fff"><rect x="8" y="2" width="28" height="34" rx="6"/><rect x="13" y="8" width="18" height="10" fill="var(--green-mid)"/><circle cx="15" cy="28" r="3" fill="var(--green-mid)"/><circle cx="29" cy="28" r="3" fill="var(--green-mid)"/><path d="M12 38l-6 10M32 38l6 10M8 44h28" stroke="#fff" stroke-width="3"/></svg>
    <h3>RAIL FREIGHT</h3>
    <p>Mauris semper vehicula orci, et mattis nulla. Cras eu enim lobortis, molestie augue nec, molestie ante. Vestibulum molestie consectetur tellus vitae feugiat. <b>Read More...</b></p>
  </div>
  <div class="service" style="left:634px;top:246px">
    <svg width="58" height="44" viewBox="0 0 58 44" fill="#fff"><path d="M4 30l44-20c6-2 9 2 4 5L14 34z"/><path d="M20 24L10 8h6l16 10zM30 24l4 16h-6l-10-12z"/><path d="M4 30l-2-8h4l6 6z"/></svg>
    <h3>AIR FREIGHT</h3>
    <p>Mauris semper vehicula orci, et mattis nulla. Cras eu enim lobortis, molestie augue nec, molestie ante. Vestibulum molestie consectetur tellus vitae feugiat. <b>Read More...</b></p>
  </div>
  <a class="btn-outline">VIEW ALL SERVICES <span>›</span></a>
</section>

<section class="partners">
  <h2 class="section-title">OUR <em>PARTNERS</em></h2>
  <div class="badges">
    <div class="badge" style="width:164px;height:30px" aria-label="Partner badge"></div>
    <div class="badge" style="width:186px;height:30px" aria-label="Partner badge"></div>
    <div class="badge" style="width:96px;height:44px" aria-label="Partner badge"></div>
    <div class="badge" style="width:182px;height:34px" aria-label="Partner badge"></div>
    <div class="badge" style="width:60px;height:58px" aria-label="Partner badge"></div>
  </div>
</section>

<section class="clients">
  <h2 class="section-title">HAPPY CLIENTS</h2>
  <p class="clients-sub">THERE CUSTOMER ARE USING CARGORA SERVICES AND, GUESS WHAT, THEY ARE HAPPY!</p>
  <blockquote class="quote">“Mauris semper vehicula orci, et mattis nulla. Cras eu enim lobortis, molestie augue nec, molestie ante. Vestibulum molestie consectetur tellus vitae feugiat. Sed eget neque in tellus interdum bibendum vitae non tellus. Praesent quam nisl, lacinia vitae sagittis et, accumsan ut lacus.”<cite>- Mr. Dario Fenwick</cite></blockquote>
  <div class="circle-arrow" style="left:383px"><svg width="8" height="10" viewBox="0 0 8 10"><path d="M6 1L2 5l4 4" stroke="#fff" stroke-width="1.6" fill="none"/></svg></div>
  <div class="thumbs">
    <div class="thumb" role="img" aria-label="Client portrait"></div>
    <div class="thumb" role="img" aria-label="Client portrait"></div>
    <div class="thumb active" role="img" aria-label="Client portrait, selected"></div>
    <div class="thumb" role="img" aria-label="Client portrait"></div>
    <div class="thumb" role="img" aria-label="Client portrait"></div>
  </div>
  <div class="circle-arrow" style="left:795px"><svg width="8" height="10" viewBox="0 0 8 10"><path d="M2 1l4 4-4 4" stroke="#fff" stroke-width="1.6" fill="none"/></svg></div>
</section>

<footer class="footer">
  <div class="col-links">
    <h4>USEFUL LINKS</h4>
    <a>Home</a><a>Services</a><a>Container</a><a>Contact</a><a>Quote (or free quote?)</a>
  </div>
  <div class="col-about">
    <h4>ABOUT CARGORA</h4>
    <p>Maecenas purus neque, tincidunt sed urna a, maximus semper nisi. Ut vel libero condimentum, posuere nunc eget, venenatis lacus. Pellentesque a imperdiet sapien.</p>
    <p>Curabitur id tristique felis. Sed sollicitudin mi a augue placerat, sed facilisis felis vestibulum. Quisque aliquam urna quis ipsum posuere feugiat. Nunc malesuada pretium eros.</p>
  </div>
  <div class="tweet"><i></i>"Curabitur id tristique felis. Sed sollicitudin mi a augue placerat"</div>
  <div class="col-news">
    <h4>LATEST NEWS</h4>
    <div class="news"><div class="date">Dec<b>04</b></div><div><p>Maecenas purus neque, tincidunt sed urna a, maximus semper nisi ut vel libero.</p><a>read more</a></div></div>
    <div class="news"><div class="date">Dec<b>04</b></div><div><p>Maecenas purus neque, tincidunt sed urna a, maximus semper nisi ut vel libero.</p><a>read more</a></div></div>
    <div class="news"><div class="date">Dec<b>04</b></div><div><p>Maecenas purus neque, tincidunt sed urna a, maximus semper nisi ut vel libero.</p><a>read more</a></div></div>
  </div>
</footer>

<div class="bottombar">
  <div class="legal"><a>TERMS OF SERVICE</a><a>PRIVACY POLICY</a><a>SITEMAP</a></div>
  <div class="copy">COPYRIGHT © 2015 VERDANQ ALLIANCE GROUP. ALL RIGHTS RESERVED</div>
</div>

</body>
</html>
```